Zielgruppe
Wir sind ein kleiner familiengeführter Weinbaubetrieb am Wagram und suchen einen modernen und naturnahen Namen und ein Etikett mit Blickfang für unseren Wermut, aus handgepflückten regionalen Wildkräutern mit Rosewein vom Zweigelt. Charakeristik des Getränks: Aperitif, Zitrusnote, leichte Bitternote, mit Tonic water als Cocktail.
Unsere Zielgruppe: kaufkräftige Genussmenschen im mittleren Alter
Aufgabenstellung
Etikett für 0,5l Flasche, Flasche noch nicht festgelegt, Etikettenhöhe: 65mm
Was soll draufstehen: Name, Vermouth, local botanicals, handcrafted, small batch

```html
<!DOCTYPE html>
<html lang="en">
<head>
<meta charset="utf-8">
<title>Krautwiese Vermouth – Rosé Vermouth Label</title>
<link rel="stylesheet" href="https://fonts.googleapis.com/css2?family=IBM+Plex+Mono:wght@400&family=Allura&display=swap">
<style>
  :root {
    --label-blush: #f6e1e1;
    --label-blush-deep: #efcfd0;
    --label-blush-light: #fbf0ef;
    --panel-white: #faf8f6;
    --frame-rose: #d9868b;
    --seal-rose: #d97c82;
    --script-rose: #d2696f;
    --ink: #2e2a2a;
  }
  * { margin: 0; padding: 0; box-sizing: border-box; }
  html, body {
    width: 828px;
    height: 1200px;
    overflow: hidden;
    background: #ffffff;
  }
  .label {
    position: relative;
    width: 828px;
    height: 1200px;
  }
  .label__marble {
    position: absolute;
    inset: 0;
    background:
      radial-gradient(ellipse 60% 40% at 20% 15%, var(--label-blush-light), transparent 70%),
      radial-gradient(ellipse 50% 35% at 85% 75%, var(--label-blush-deep), transparent 70%),
      radial-gradient(ellipse 55% 40% at 30% 90%, var(--label-blush-light), transparent 70%),
      linear-gradient(160deg, var(--label-blush) 0%, var(--label-blush-deep) 50%, var(--label-blush) 100%);
  }
  .label__panel {
    position: absolute;
    left: 100px;
    top: 213px;
    width: 630px;
    height: 816px;
    background: var(--panel-white);
    border: 3px solid var(--frame-rose);
    text-align: center;
  }
  .brand-name {
    position: absolute;
    top: 50px;
    left: 0;
    right: 0;
    font-family: "IBM Plex Mono", monospace;
    font-size: 40px;
    color: var(--ink);
    letter-spacing: 0.5px;
  }
  .brand-seal {
    position: absolute;
    top: 147px;
    left: 50%;
    width: 172px;
    height: 172px;
    margin-left: -86px;
    border-radius: 50%;
    background: var(--seal-rose);
  }
  .product-title {
    position: absolute;
    top: 340px;
    left: 0;
    right: 0;
    font-family: "Allura", cursive;
    font-size: 130px;
    line-height: 0.85;
    color: var(--script-rose);
  }
  .product-title__line--first { display: block; padding-left: 40px; }
  .product-title__line--second { display: block; padding-left: 70px; }
  .product-description {
    position: absolute;
    top: 648px;
    left: 0;
    right: 0;
    font-family: "IBM Plex Mono", monospace;
    font-size: 35px;
    line-height: 43px;
    color: var(--ink);
  }
</style>
</head>
<body>
  <main class="label">
    <div class="label__marble" role="img" aria-label="Soft pink marbled paper texture"></div>
    <section class="label__panel">
      <h1 class="brand-name">Krautwiese Vermouth</h1>
      <div class="brand-seal" aria-hidden="true"></div>
      <h2 class="product-title">
        <span class="product-title__line--first">Rose</span>
        <span class="product-title__line--second">Vermouth</span>
      </h2>
      <p class="product-description">Handcrafted Small Batch<br>Vermouth with Rose Wine &amp;<br>local Botanicals</p>
    </section>
  </main>
</body>
</html>
```